Special offers flyer for IT firm

We need a flyer design for our IT technical services firm based in Melbourne, Australia. We want to advertise two offerings on a double sided flyer.
-
First Offering:
Free computer system health report and audit
- health check of servers, workstations and network
- comprehensive non-technical report including recommendations
-
Second Offering:
Discounted technical support - $80* per hour
- day to day helpdesk support
- system upgrades and migrations
- cloud services design, implementation and support
- web hosting, domain names and email filtering

*exclusive of GST (must denote somewhere in small print)
-
The contact details for the offer must include room for Phone, Email and Web Address.

I am not set on the text, or any particular format, additional images would be good to break up the pages.

Target Market(s)

Professional Services small business owners (under 30 staff)

Industry/Entity Type

Computer

Requirements
Must have
• DL Sized document (210mmx99mm) portrait or landscape, double sided.

```html
<!DOCTYPE html>
<html lang="en">
<head>
<meta charset="utf-8">
<title>Northbay IT – Special Offers Flyer</title>
<link rel="stylesheet" href="https://fonts.googleapis.com/css2?family=Tinos:wght@400;700&display=swap">
<style>
  :root {
    --ink-blue: #1d5c9c;
    --brand-dark: #1c1c1c;
    --band-blue: #1e67a8;
    --offer-red: #d0161c;
    --offer-cyan: #1fb3e6;
    --paper: #ffffff;
    --mist: #e6f2fa;
  }
  * { box-sizing: border-box; margin: 0; padding: 0; }
  html, body { width: 1200px; height: 1200px; overflow: hidden; background: var(--paper); }
  body { font-family: "Tinos", "Times New Roman", serif; color: var(--ink-blue); }

  .flyer {
    position: relative; width: 1200px; height: 1200px; overflow: hidden;
    background:
      radial-gradient(ellipse 720px 170px at 640px 230px, var(--mist), transparent 70%),
      radial-gradient(ellipse 820px 190px at 600px 700px, var(--mist), transparent 70%),
      var(--paper);
  }

  .brand { position: absolute; color: var(--brand-dark); font-weight: 400; white-space: nowrap; display: flex; align-items: center; gap: 14px; line-height: 1; }
  .brand-mark { border-radius: 50%; background: var(--ink-blue); flex: none; }
  .brand--header { left: 56px; top: 136px; font-size: 84px; }
  .brand--header .brand-mark { width: 22px; height: 22px; }
  .brand--footer { left: 64px; top: 1026px; font-size: 42px; }
  .brand--footer .brand-mark { width: 14px; height: 14px; }

  .contact-box {
    position: absolute; left: 591px; top: 83px; width: 522px; height: 128px;
    background: var(--band-blue); color: var(--paper); text-align: center;
    padding-top: 12px;
  }
  .contact-box .web { font-size: 49px; line-height: 1.1; }
  .contact-box .details { font-size: 26px; line-height: 1.3; }

  .offer-title { position: absolute; font-weight: 400; white-space: nowrap; line-height: 1; }
  .offer-title--one { left: 56px; top: 250px; font-size: 52px; }
  .offer-title--two { left: 64px; top: 664px; font-size: 52px; }

  .offer-points { position: absolute; list-style: none; font-size: 37px; line-height: 45px; white-space: nowrap; }
  .offer-points--one { left: 67px; top: 317px; }
  .offer-points--one li { margin-bottom: 22px; }
  .offer-points--two { left: 62px; top: 733px; }
  .offer-points--two li { margin-bottom: 18px; }

  .photo {
    position: absolute; border-radius: 50%; border: 4px solid var(--paper);
    box-shadow: 0 0 0 2px var(--band-blue);
  }
  .photo--network { left: 736px; top: 382px; width: 182px; height: 182px; background: radial-gradient(circle at 50% 45%, #5aa2d8, #cfe6f6 70%); }
  .photo--monitor { left: 887px; top: 300px; width: 200px; height: 200px; background: radial-gradient(circle at 45% 50%, #2d7fc8, #cfd8e0 75%); }
  .photo--help-key { left: 962px; top: 793px; width: 174px; height: 174px; background: radial-gradient(circle at 45% 50%, #d6322c 0 22%, #d9dde2 45%, #8e969e); }
  .photo--cloud-key { left: 856px; top: 910px; width: 154px; height: 154px; background: radial-gradient(circle at 45% 45%, #38b3e6 0 30%, #c9ced4 60%, #7e868d); }

  .corner-tag { position: absolute; width: 160px; height: 160px; }

  .fine-print { position: absolute; left: 337px; top: 1052px; font-size: 18px; color: var(--brand-dark); }

  .footer-band {
    position: absolute; left: 53px; top: 1090px; width: 1084px; height: 48px;
    background: var(--band-blue); color: var(--paper);
    font-size: 42px; line-height: 48px; padding-left: 10px; white-space: nowrap;
  }
</style>
</head>
<body>
<main class="flyer">
  <div class="brand brand--header"><span class="brand-mark"></span>Northbay IT</div>

  <div class="contact-box">
    <p class="web">www.northbay-it.com</p>
    <p class="details">T: 035550172, E:sales@northbay-it.com</p>
  </div>

  <section class="offer offer--audit">
    <h2 class="offer-title offer-title--one">Free computer system health report and audit</h2>
    <ul class="offer-points offer-points--one">
      <li>- health check of servers workstations<br>&nbsp;&nbsp;and network</li>
      <li>- comprehensive non-technical report<br>&nbsp;&nbsp;including recommendations</li>
    </ul>
    <div class="photo photo--network" role="img" aria-label="Photo of a computer network with linked workstations"></div>
    <div class="photo photo--monitor" role="img" aria-label="Photo of a desktop monitor and computer tower"></div>
    <svg class="corner-tag" style="left:1009px; top:430px;" viewBox="0 0 160 160" aria-label="Offer 1">
      <polygon points="0,160 160,160 160,0" fill="var(--offer-red)"/>
      <text x="88" y="108" fill="#fff" font-family="Tinos, serif" font-size="22" text-anchor="middle" transform="rotate(-45 88 108)">Offer</text>
      <text x="120" y="124" fill="#fff" font-family="Tinos, serif" font-size="24" text-anchor="middle" transform="rotate(-45 120 124)">1</text>
    </svg>
  </section>

  <section class="offer offer--support">
    <h2 class="offer-title offer-title--two">Discounted technical support - $80* per hour</h2>
    <ul class="offer-points offer-points--two">
      <li>- day to day helpdesk support</li>
      <li>- system upgrades and migrations</li>
      <li>- cloud services design, implementation and support</li>
      <li>- web hosting, domain names and email filtering</li>
    </ul>
    <svg class="corner-tag" style="left:1009px; top:617px;" viewBox="0 0 160 160" aria-label="Offer 2">
      <polygon points="0,0 160,0 160,160" fill="var(--offer-cyan)"/>
      <text x="118" y="38" fill="#fff" font-family="Tinos, serif" font-size="22" text-anchor="middle" transform="rotate(45 118 38)">Offer</text>
      <text x="100" y="70" fill="#fff" font-family="Tinos, serif" font-size="24" text-anchor="middle" transform="rotate(45 100 70)">2</text>
    </svg>
    <div class="photo photo--help-key" role="img" aria-label="Photo of a keyboard with a red Help key"></div>
    <div class="photo photo--cloud-key" role="img" aria-label="Photo of a keyboard with a blue cloud key"></div>
  </section>

  <div class="brand brand--footer"><span class="brand-mark"></span>Northbay IT</div>
  <p class="fine-print">*exclusive of GST</p>

  <footer class="footer-band">www.northbay-it.com T:035550172, E:sales@northbay-it.com</footer>
</main>
</body>
</html>
```